Brightway Gate works Business cards/Stationery
Business cards and stationery
Brightway Gate works Business cards/Stationery -
Creative Brief
Use specific fonts
Whatever you think looks best
Professional
Paul Hendley
Owner
248 Marlow Ridge Rd. Brookvale, SC 29642
Brightwaygateworks@mailnest.net
www.Brightwaygateworks.net
Use tagline: A Bright Way In Every Day
I would like to see something unique with the logo on the back.

```html
<!DOCTYPE html>
<html lang="en">
<head>
<meta charset="utf-8">
<title>Brightway Gate works – Business Card</title>
<link href="https://fonts.googleapis.com/css2?family=Open+Sans:ital,wght@0,400;0,600;0,700;1,700&display=swap" rel="stylesheet">
<style>
  :root{
    --page:#e9e6e1;
    --card:#ffffff;
    --ink:#2a2a2a;
    --brand-red:#8e1f26;
    --band-dark:#3a0d10;
    --band-mid:#7a1d23;
    --rule:#9a9a9a;
  }
  *{margin:0;padding:0;box-sizing:border-box}
  html,body{width:1200px;height:965px;overflow:hidden}
  body{background:var(--page);font-family:"Open Sans",Arial,sans-serif;color:var(--ink);position:relative}
  .card{
    position:absolute;left:160px;top:232px;width:880px;height:500px;
    background:var(--card);border-radius:24px;overflow:hidden;
    box-shadow:0 8px 24px rgba(0,0,0,.18);
  }
  .brand{
    position:absolute;left:0;right:0;top:58px;
    display:flex;align-items:center;justify-content:center;gap:18px;
  }
  .brand-mark{width:44px;height:44px;background:var(--brand-red)}
  .brand-name{font-weight:700;font-size:50px;letter-spacing:1px;text-transform:uppercase;color:var(--ink);line-height:1}
  .person{position:absolute;right:580px;top:218px;text-align:right}
  .person-name{font-size:32px;font-weight:600;color:var(--brand-red);line-height:1.1}
  .person-role{font-size:20px;font-weight:700;line-height:1.3;margin-bottom:14px}
  .person-address{font-size:21px;line-height:1.6}
  .divider{position:absolute;left:330px;top:224px;width:1px;height:140px;background:var(--rule)}
  .contacts{position:absolute;left:360px;top:218px;list-style:none}
  .contacts li{display:flex;align-items:center;gap:14px;font-size:21px;height:37px}
  .contacts svg{width:20px;height:20px;flex:none}
  .band{position:absolute;left:0;top:0;width:880px;height:500px}
  .tagline{
    position:absolute;left:0;right:0;bottom:24px;text-align:center;
    font-style:italic;font-weight:700;font-size:24px;color:#fff;letter-spacing:.5px;
  }
</style>
</head>
<body>
  <div class="card">
    <svg class="band" viewBox="0 0 880 500" aria-hidden="true">
      <defs>
        <linearGradient id="bandFill" x1="0" y1="0" x2="1" y2="0">
          <stop offset="0" stop-color="#3a0d10"/>
          <stop offset=".5" stop-color="#7a1d23"/>
          <stop offset="1" stop-color="#3a0d10"/>
        </linearGradient>
      </defs>
      <path d="M0,378 C220,392 520,440 880,418 L880,500 L0,500 Z" fill="url(#bandFill)"/>
      <path d="M0,360 C240,376 540,428 880,410" fill="none" stroke="#111" stroke-width="3"/>
      <path d="M0,366 C240,384 540,434 880,414 L880,420 C540,442 240,392 0,378 Z" fill="#fff"/>
    </svg>

    <div class="brand">
      <span class="brand-mark"></span>
      <span class="brand-name">Brightway Gate works</span>
    </div>

    <div class="person">
      <p class="person-name">Paul Hendley</p>
      <p class="person-role">Owner</p>
      <p class="person-address">248 Marlow Ridge Rd.<br>Brookvale, SC 29642</p>
    </div>

    <div class="divider"></div>

    <ul class="contacts">
      <li>
        <svg viewBox="0 0 24 24"><path fill="var(--brand-red)" d="M6.6 10.8a15 15 0 0 0 6.6 6.6l2.2-2.2c.3-.3.7-.4 1-.2 1.1.4 2.3.6 3.6.6.6 0 1 .4 1 1V20c0 .6-.4 1-1 1A17 17 0 0 1 3 4c0-.6.4-1 1-1h3.5c.6 0 1 .4 1 1 0 1.3.2 2.5.6 3.6.1.3 0 .7-.2 1z"/></svg>
        (864) 555-0142
      </li>
      <li>
        <svg viewBox="0 0 24 24"><rect x="6" y="3" width="12" height="6" fill="var(--brand-red)"/><rect x="3" y="9" width="18" height="8" rx="1" fill="var(--brand-red)"/><rect x="7" y="14" width="10" height="7" fill="#fff" stroke="var(--brand-red)" stroke-width="2"/></svg>
        (864) 555-0187
      </li>
      <li>
        <svg viewBox="0 0 24 24"><circle cx="12" cy="12" r="4" fill="none" stroke="var(--ink)" stroke-width="2.4"/><path d="M16 8v5a2.5 2.5 0 0 0 5 0v-1a9 9 0 1 0-4 7.5" fill="none" stroke="var(--ink)" stroke-width="2.4"/></svg>
        Brightwaygateworks@mailnest.net
      </li>
      <li>
        <svg viewBox="0 0 24 24"><circle cx="12" cy="12" r="9" fill="none" stroke="var(--brand-red)" stroke-width="2"/><path d="M3 12h18M12 3c3 3 3 15 0 18M12 3c-3 3-3 15 0 18" fill="none" stroke="var(--brand-red)" stroke-width="1.6"/></svg>
        www.Brightwaygateworks.net
      </li>
    </ul>

    <p class="tagline">A Bright Way In Every Day</p>
  </div>
</body>
</html>
```